Design an Event Flyer template for Chapter Events

Dear Freelancer,

We are a small chapter around cloud security and we are organizing local chapter events throughout the year. The current event flyer doesn't cut it anymore I would like something fresh and more fitting to what we do.

For the upcoming event around bit-coins I would like to have a new flyer template. The template then can be used for the other events we will be holding.
It must be editable in word since I don't have any design software available. Also think about an easy template to deal with i.e. if we have less speakers at an event for instance. It should be easy to remove a speaker or add another topic for instance.

I also want a participation certificate template to use on the events to hand out to the participants. This template should also have the same look and feel as the event flyer. The additionally I would like to have an e-mail signature with the event details and the Chapter logo in it.

Three things in this Freelance offer:
- New flyer template (word)
- participation certificate based on the same look and feel of the event template also as a template but maybe PPT
- e-mail signature

If you need any logo or vector works I can buy them at pixelmarrowdotnet

You will have the following information at your hand:
- The old event flyer in PDF
- The Chapter logos
- Sample certificate of participation

This is an opportunity for the best design to earn more in a long time relationship with our chapter.

NOTE: I like creativity, don't just copy the sample i showed. It should have a cloudy security feeling.

```html
<!DOCTYPE html>
<html lang="en">
<head>
<meta charset="utf-8">
<title>Nimbusward – Chapter event 2014</title>
<link rel="stylesheet" href="https://fonts.googleapis.com/css2?family=Comfortaa:wght@600;700&family=Arimo:wght@400;700&display=swap">
<style>
  :root{
    --blue-deep:#1b6fb8;
    --blue-sky:#27a8e0;
    --blue-bubble:#1593dc;
    --ink:#333333;
    --text-blue:#2b5c9a;
    --orange-light:#f7d47e;
    --orange-mid:#e9a935;
    --orange-deep:#d47e13;
    --grey-card:#e6e7e9;
    --grey-side:#c9cacc;
    --photo:#58595b;
    --white:#ffffff;
  }
  *{box-sizing:border-box;margin:0;padding:0}
  html,body{width:848px;height:1200px;overflow:hidden;background:var(--white)}
  .flyer{position:relative;width:848px;height:1200px;overflow:hidden;font-family:"Arimo",Arial,sans-serif;color:var(--text-blue)}
  .abs{position:absolute}
  .sky{left:0;top:0}
  .brand-mark{left:104px;top:110px;width:46px;height:46px;border-radius:50%;background:var(--white)}
  .brand-name{left:166px;top:106px;font-family:"Comfortaa",sans-serif;font-weight:700;font-size:48px;line-height:54px;color:var(--white);letter-spacing:1px}
  .title{left:100px;top:264px;font-family:"Comfortaa",sans-serif;font-weight:700;font-size:53px;line-height:60px;color:var(--ink);letter-spacing:1px;white-space:nowrap}
  .info-card{left:22px;top:366px}
  .bubble{width:86px;height:56px}
  .bubble-label{position:absolute;left:0;top:8px;width:86px;text-align:center;color:var(--white);font-weight:700;font-size:16px}
  .info-text{font-size:16.5px;line-height:20px;color:var(--text-blue)}
  .timeline-rail{left:376px;top:320px;width:11px;height:746px;background:var(--blue-deep)}
  .arrow{left:384px;width:44px;height:22px}
  .slot{width:82px;height:82px;border-radius:50%;background:var(--white);border:2px solid var(--blue-deep);display:flex;align-items:center;justify-content:center;font-weight:700;font-size:13px;color:var(--ink)}
  .topic{width:172px;height:116px}
  .topic-text{position:absolute;font-size:11px;line-height:12.5px;color:#5a3a07}
  .topic-text.closing{font-weight:700;font-size:13px;color:#1f1f1f}
  .speakers{left:680px;top:268px;width:168px;height:832px;background:linear-gradient(90deg,var(--orange-light),#f0c25e 45%,var(--orange-deep))}
  .speakers-head{position:absolute;left:0;top:14px;width:100%;text-align:center;font-family:"Comfortaa",sans-serif;font-weight:700;font-size:19px;color:var(--ink)}
  .speaker-photo{width:88px;height:88px;background:var(--photo);border:4px solid var(--white);border-radius:4px;box-shadow:2px 3px 5px rgba(0,0,0,.35);display:flex;align-items:center;justify-content:center;color:var(--white);font-size:16px}
  .speaker-meta{width:88px;text-align:center;font-size:11px;line-height:13px;color:#3b3b3b}
  .register{left:0;top:1106px;width:848px;height:94px;background:linear-gradient(180deg,var(--blue-sky),#1e96d6);color:var(--white);padding:20px 0 0 46px}
  .register h2{font-size:16.5px;font-weight:700}
  .register p{font-size:13px;line-height:16px}
</style>
</head>
<body>
<div class="flyer">

  <svg class="abs sky" width="848" height="300" viewBox="0 0 848 300">
    <defs>
      <linearGradient id="skyGrad" x1="0" y1="0" x2="0" y2="1">
        <stop offset="0" stop-color="#1a6cb6"/><stop offset="1" stop-color="#2aa3df"/>
      </linearGradient>
    </defs>
    <path d="M0 0H848V240Q560 150 0 248Z" fill="url(#skyGrad)"/>
  </svg>

  <div class="abs brand-mark" aria-hidden="true"></div>
  <div class="abs brand-name">Nimbusward</div>

  <div class="abs title">Chapter event 2014</div>

  <svg class="abs info-card" width="340" height="700" viewBox="0 0 340 700" aria-hidden="true">
    <defs>
      <linearGradient id="cardGrad" x1="0" y1="0" x2="1" y2="0">
        <stop offset="0" stop-color="#d4d5d7"/><stop offset=".35" stop-color="#f7f7f8"/><stop offset="1" stop-color="#e4e5e7"/>
      </linearGradient>
    </defs>
    <path d="M0 0H318L340 16V700H22L0 684Z" fill="#bfc0c2"/>
    <path d="M0 0H318L340 16H22Z" fill="#e3e4e6"/>
    <path d="M0 0L22 16V700L0 684Z" fill="var(--grey-side)"/>
    <rect x="22" y="16" width="318" height="684" fill="url(#cardGrad)"/>
  </svg>

  <svg width="0" height="0" style="position:absolute">
    <defs>
      <symbol id="speech" viewBox="0 0 86 56">
        <path d="M8 0H78Q86 0 86 8V34Q86 42 78 42H48L62 56L30 42H8Q0 42 0 34V8Q0 0 8 0Z" fill="var(--blue-bubble)"/>
      </symbol>
      <symbol id="folder" viewBox="0 0 172 116">
        <path d="M10 6H70Q80 6 86 16V22H162Q172 22 172 32V104Q172 116 160 116H12Q0 116 0 104V16Q0 6 10 6Z" fill="#d9890f"/>
        <path d="M10 32H64Q76 32 82 20Q88 8 100 8H160Q172 8 172 20V104Q172 116 160 116H12Q0 116 0 104V44Q0 32 10 32Z" fill="#f2b833"/>
        <path d="M10 32H64Q76 32 82 20Q88 8 100 8H160Q172 8 172 20V30H0Q2 32 10 32Z" fill="#f7cf66" opacity=".6"/>
      </symbol>
      <symbol id="arrow" viewBox="0 0 44 22">
        <path d="M0 7H24V0L44 11L24 22V15H0Z" fill="var(--blue-deep)"/>
      </symbol>
    </defs>
  </svg>

  <div class="abs" style="left:93px;top:429px"><svg class="bubble"><use href="#speech"/></svg><span class="bubble-label">When?</span></div>
  <p class="abs info-text" style="left:105px;top:504px">Friday,18th of October<br>13.00 -17.00</p>

  <div class="abs" style="left:226px;top:564px"><svg class="bubble"><use href="#speech"/></svg><span class="bubble-label">Where?</span></div>
  <p class="abs info-text" style="left:100px;top:627px">Alpenlink (Schweiz) AG<br>text text text text text text<br>text text text text</p>

  <div class="abs" style="left:93px;top:717px"><svg class="bubble"><use href="#speech"/></svg><span class="bubble-label">Why?</span></div>
  <p class="abs info-text" style="left:95px;top:787px">Meet and Greet<br>text text text text text text text<br>text text text text text text text<br>text text text text</p>

  <div class="abs" style="left:226px;top:867px"><svg class="bubble"><use href="#speech"/></svg><span class="bubble-label">Costs?</span></div>
  <p class="abs info-text" style="left:97px;top:943px">Members<br>Others</p>

  <div class="abs timeline-rail"></div>

  <svg class="abs arrow" style="top:394px"><use href="#arrow"/></svg>
  <svg class="abs arrow" style="top:526px"><use href="#arrow"/></svg>
  <svg class="abs arrow" style="top:658px"><use href="#arrow"/></svg>
  <svg class="abs arrow" style="top:789px"><use href="#arrow"/></svg>
  <svg class="abs arrow" style="top:941px"><use href="#arrow"/></svg>
  <svg class="abs arrow" style="top:1043px"><use href="#arrow"/></svg>

  <svg class="abs topic" style="left:478px;top:338px"><use href="#folder"/></svg>
  <p class="abs topic-text" style="left:490px;top:392px">Introduction text<br>Introduction text,Introduction<br>Introduction text text,</p>
  <svg class="abs topic" style="left:478px;top:468px"><use href="#folder"/></svg>
  <p class="abs topic-text" style="left:490px;top:531px">Cloud cloud cloud<br>Cloud cloud cloud<br>Cloud cloud cloud</p>
  <svg class="abs topic" style="left:478px;top:598px"><use href="#folder"/></svg>
  <p class="abs topic-text" style="left:495px;top:661px">Cloud cloud cloud<br>Cloud cloud cloud<br>Cloud cloud cloud</p>
  <svg class="abs topic" style="left:478px;top:727px"><use href="#folder"/></svg>
  <p class="abs topic-text" style="left:499px;top:791px">Cloud cloud cloud<br>Cloud cloud cloud<br>Cloud cloud cloud</p>
  <svg class="abs topic" style="left:478px;top:855px"><use href="#folder"/></svg>
  <p class="abs topic-text" style="left:504px;top:922px">Cloud cloud cloud<br>Cloud cloud cloud<br>Cloud cloud cloud</p>
  <svg class="abs topic" style="left:478px;top:983px"><use href="#folder"/></svg>
  <p class="abs topic-text closing" style="left:504px;top:1045px">Closing Talk</p>

  <div class="abs slot" style="left:406px;top:317px">14.00-14.30</div>
  <div class="abs slot" style="left:406px;top:447px">14.00-14.30</div>
  <div class="abs slot" style="left:406px;top:576px">14.00-14.30</div>
  <div class="abs slot" style="left:406px;top:708px">14.00-14.30</div>
  <div class="abs slot" style="left:406px;top:837px">14.00-14.30</div>
  <div class="abs slot" style="left:406px;top:962px">14.00-14.30</div>

  <aside class="abs speakers">
    <h3 class="speakers-head">Speaker</h3>
  </aside>
  <div class="abs speaker-photo" style="left:723px;top:330px" role="img" aria-label="Speaker portrait photo">photo</div>
  <p class="abs speaker-meta" style="left:723px;top:432px">Name<br>Title</p>
  <div class="abs speaker-photo" style="left:723px;top:465px" role="img" aria-label="Speaker portrait photo">photo</div>
  <p class="abs speaker-meta" style="left:723px;top:566px">Name<br>Title</p>
  <div class="abs speaker-photo" style="left:723px;top:599px" role="img" aria-label="Speaker portrait photo">photo</div>
  <p class="abs speaker-meta" style="left:723px;top:701px">Name<br>Title</p>
  <div class="abs speaker-photo" style="left:723px;top:733px" role="img" aria-label="Speaker portrait photo">photo</div>
  <p class="abs speaker-meta" style="left:723px;top:835px">Name<br>Title</p>
  <div class="abs speaker-photo" style="left:723px;top:870px" role="img" aria-label="Speaker portrait photo">photo</div>
  <p class="abs speaker-meta" style="left:723px;top:971px">Name<br>Title</p>

  <footer class="abs register">
    <h2>How to register?</h2>
    <p>asdgffghggfjghjhjgv hjkmjkhj gdgdggfgfdg gdfgfg dfssfhg<br>dsfsdfdsf&nbsp; email: hello@nimbusward.ch</p>
  </footer>
</div>
</body>
</html>
```